・書籍主題=港町に残る古い灯台守の日誌
副題=潮風が運んだ便りの行方
・著者名=柳瀬直之(やなせ なおゆき)

・仕様
四六・上製・310ページ
タテ組み(右綴じ)

※デザインは基本的にデザイナーさんにお任せしますが、学術研究書であるという点を念頭に置き製作してください。

画像を数点提示いたしますのでご参照下さい。
本書で取り上げている時代のディベートの風景です。
(提示画像は低解像度となっています。実際当選作品には高解像度の画像を支給させて頂く予定です)
【キャプション】
・写真番号2  雑誌『青嶺』10月号 1933(昭和8)年発行
・写真番号4-① 雑誌『青嶺』12月号 1933(昭和8)年発行
・写真番号7  雑誌『青嶺』3月号  1935(昭和10)年発行
・写真番号8  雑誌『青嶺』4月号  1935(昭和10)年発行

これらの画像をデザインに織り込んで頂いても構いませんし、まったく別の独自視点による作成も歓迎いたします。
記載項目
書名・著者名・出版社名(朔風社)

ISBN978-4-91572-108-3 C1021

背景等に光線を入れた作品(暗めのバックに光を入れる等)をイメージしていますが、デザイナーさんの目線で本書のイメージから自由にデザインをして頂けますと幸いです。
• シンプル
複雑
• 単色
カラフル
• 暗い
明るい
• 日常
高級
• 遊び心
厳粛
• 未来的
伝統的
• 女性的
男性的
画像のアプロードが遅くなり申し訳ありません。
(7/24追記)
画像ファイル名は下記の通りです。
・33→写真番号2
・66→写真番号4-①
・247→写真番号7
・315→写真番号8

募集時の著者のイメージに最も近く、また、提供画像を的確に配置して下さっている点等を評価し、本提案を採用させて頂くこととなりました。

この度もたくさんのご応募を頂戴し、心より感謝いたします。
どの作品も著者と出版社の意図をよくくみ取っていただき、素敵なものばかりでとても迷ったのですが、イメージに近かった作品を採用させて頂きました。
今後も色々な著作のブックカバーの依頼をさせて頂きたく思いますので、引き続きよろしくお願いいたします。

```html
<!DOCTYPE html>
<html lang="ja">
<head>
<meta charset="utf-8">
<title>港町に残る古い灯台守の日誌</title>
<link rel="stylesheet" href="https://fonts.googleapis.com/css2?family=Noto+Sans+JP:wght@900&family=Noto+Serif+JP:wght@500;700&display=swap">
<style>
  :root {
    --ground: #3a3a3a;
    --ground-deep: #2b2b2b;
    --title-yellow: #f4d80c;
    --ink-white: #f2f2f2;
    --rule: #d8d8d8;
    --photo-light: #b9b9b9;
    --photo-mid: #6e6e6e;
    --photo-dark: #242424;
  }
  html, body {
    margin: 0;
    padding: 0;
    overflow: hidden;
    background: var(--ground);
  }
  .cover {
    position: relative;
    width: 811px;
    height: 1200px;
    overflow: hidden;
    background: var(--ground);
    font-family: "Noto Serif JP", serif;
    color: var(--ink-white);
  }
  .archive-photo {
    position: absolute;
    left: 0;
    top: 24px;
    width: 811px;
    height: 548px;
    background:
      radial-gradient(ellipse 55% 45% at 62% 38%, var(--photo-light) 0%, rgba(150,150,150,0.6) 35%, rgba(90,90,90,0) 75%),
      linear-gradient(180deg, var(--photo-mid) 0%, #555 55%, var(--photo-dark) 100%);
    filter: grayscale(1);
  }
  .archive-photo::after {
    content: "";
    position: absolute;
    inset: 0;
    background: linear-gradient(180deg, rgba(58,58,58,0) 70%, var(--ground) 100%);
  }
  .series-heading {
    position: absolute;
    left: 22px;
    top: 6px;
    margin: 0;
    font-family: "Noto Serif JP", serif;
    font-weight: 700;
    font-size: 27px;
    letter-spacing: 1px;
    color: var(--ink-white);
  }
  .rule {
    position: absolute;
    left: 0;
    width: 811px;
    height: 2px;
    background: var(--rule);
  }
  .rule-top { top: 608px; }
  .rule-bottom { top: 890px; }
  .rule-author { top: 1044px; height: 1px; }
  .book-title {
    position: absolute;
    left: 0;
    top: 620px;
    width: 811px;
    margin: 0;
    text-align: center;
    font-family: "Noto Sans JP", sans-serif;
    font-weight: 900;
    font-size: 58px;
    line-height: 88px;
    color: var(--title-yellow);
  }
  .book-subtitle {
    position: absolute;
    left: 0;
    top: 810px;
    width: 811px;
    margin: 0;
    text-align: center;
    font-weight: 500;
    font-size: 34px;
    letter-spacing: 2px;
    color: var(--ink-white);
  }
  .author {
    position: absolute;
    left: 0;
    top: 1060px;
    width: 811px;
    display: flex;
    justify-content: center;
    align-items: center;
    gap: 10px;
  }
  .author-name {
    font-weight: 500;
    font-size: 38px;
    letter-spacing: 8px;
  }
  .author-roman {
    font-size: 13px;
    line-height: 15px;
    font-style: italic;
    color: var(--ink-white);
  }
</style>
</head>
<body>
  <div class="cover">
    <div class="archive-photo" role="img" aria-label="当時の討論会の会場を写した白黒の記録写真"></div>
    <p class="series-heading">OLD LIGHTHOUSE KEEPER'S DIARY</p>

    <div class="rule rule-top"></div>
    <h1 class="book-title">港町に残る古い<br>灯台守の日誌</h1>
    <p class="book-subtitle">潮風が運んだ便りの行方</p>
    <div class="rule rule-bottom"></div>

    <div class="rule rule-author"></div>
    <div class="author">
      <span class="author-name">柳瀬直之</span>
      <span class="author-roman">Naoyuki<br>Yanase</span>
    </div>
  </div>
</body>
</html>
```